Computer screen desktop background design for dentists orthodontic office PCs

We need a new design to use as the Windows desktop background picture for the PC workstations in a dentists orthodontic office.
The design should be vector graphics.
The aspect ratio should reflect the monitor size (Resolution: 1920x1200).
In the uploaded files you can find the logo, the fonts and the design of the business card.
The design should not be brighter than the Windows 10 background picture (monitor lifetime).

The office logo must be the dominating part of the design (see uploaded files).

You don't need to use the same fonts, but the used fonts have to be in harmony with the fonts used in the logo and the business card.
The colors used have to be in harmony with the logo.
All the text below must be on the design.
The logical text groups are separated by empty lines.

Kieferorthopädie Tannwiese

Dr. med. dent. Lukas Brenner
Fachzahnarzt für Kieferorthopädie (CH) (Important information!)

Please make something cool and modern that attracts the patient's attraction when seen on the monitor screen.

Target Market(s)

dentists orthodontic office

Industry/Entity Type

Computer

Font styles to use
Sans Serif

Colors

Designer to choose colors to be used in the design.

Requirements
Must have
• The design should be vector graphics.
• The aspect ratio should reflect the monitor size (Resolution: 1920x1200).
• In the uploaded files you can find the logo, the fonts and the design of the business card.
• The design should not be brighter than the Windows 10 background picture (monitor lifetime).
• The office logo must be the dominating part of the design (see uploaded files).
• You don't need to use the same fonts, but the used fonts have to be in harmony with the fonts used in the logo and the business card.
• The colors used have to be in harmony with the logo.
• All the text below must be on the design.
• The logical text groups are separated by empty lines.
• Kieferorthopädie Tannwiese
• Dr. med. dent. Lukas Brenner
• Fachzahnarzt für Kieferorthopädie (CH) (Important information!)
• Adobe Illustrator source files
Nice to have
• Please make something cool and modern that attracts the patient's attraction when seen on the monitor screen.
Should not have

```html
<!DOCTYPE html>
<html lang="de">
<head>
<meta charset="utf-8">
<title>Kieferorthopädie Tannwiese – Desktop</title>
<link rel="stylesheet" href="https://fonts.googleapis.com/css2?family=Roboto:wght@400;700&display=swap">
<style>
  :root {
    --navy: #23215f;
    --deep: #1e2260;
    --mid: #2f6aa3;
    --sky: #3fabe2;
    --white: #ffffff;
    --veil: rgba(255, 255, 255, 0.09);
    --veil-text: rgba(255, 255, 255, 0.16);
  }
  html, body {
    margin: 0;
    padding: 0;
    width: 1200px;
    height: 750px;
    overflow: hidden;
    background: var(--white);
  }
  .wallpaper {
    position: relative;
    width: 1200px;
    height: 750px;
    overflow: hidden;
    font-family: "Roboto", Arial, sans-serif;
  }
  .wallpaper__backdrop {
    position: absolute;
    inset: 0;
  }
  .emblem {
    position: absolute;
    left: 135px;
    top: 95px;
    width: 480px;
    height: 480px;
    border-radius: 50%;
    background: var(--veil);
    display: flex;
    align-items: center;
    justify-content: center;
  }
  .emblem__name {
    font-size: 30px;
    font-weight: 700;
    color: var(--veil-text);
    white-space: nowrap;
  }
  .practice__marker {
    position: absolute;
    left: 708px;
    top: 652px;
    width: 76px;
    height: 76px;
    border-radius: 50%;
    background: linear-gradient(135deg, var(--navy), var(--sky));
  }
  .practice__name {
    position: absolute;
    left: 815px;
    top: 634px;
    margin: 0;
    font-size: 28px;
    font-weight: 700;
    color: var(--navy);
    line-height: 32px;
    white-space: nowrap;
  }
  .practice__doctor {
    position: absolute;
    left: 815px;
    top: 680px;
    margin: 0;
    font-size: 22px;
    font-weight: 400;
    letter-spacing: 0.4px;
    color: var(--sky);
    line-height: 26px;
    white-space: nowrap;
  }
  .practice__title {
    position: absolute;
    left: 815px;
    top: 705px;
    margin: 0;
    font-size: 19px;
    font-weight: 400;
    letter-spacing: 0.2px;
    color: var(--sky);
    line-height: 24px;
    white-space: nowrap;
  }
  .contact {
    position: absolute;
    left: 33px;
    top: 704px;
    display: flex;
    align-items: center;
    gap: 12px;
    color: var(--sky);
    font-size: 26px;
    font-weight: 400;
    line-height: 30px;
  }
  .contact__icon {
    width: 32px;
    height: 28px;
  }
</style>
</head>
<body>
<main class="wallpaper">
  <svg class="wallpaper__backdrop" width="1200" height="750" viewBox="0 0 1200 750" aria-hidden="true">
    <defs>
      <linearGradient id="sky-gradient" x1="0" y1="0" x2="1200" y2="750" gradientUnits="userSpaceOnUse">
        <stop offset="0" stop-color="#1e2260"/>
        <stop offset="0.5" stop-color="#2f6aa3"/>
        <stop offset="1" stop-color="#3fb0e6"/>
      </linearGradient>
      <filter id="wave-shadow" x="-10%" y="-20%" width="120%" height="140%">
        <feGaussianBlur stdDeviation="7"/>
      </filter>
    </defs>
    <rect width="1200" height="750" fill="url(#sky-gradient)"/>
    <path d="M0,612 C150,672 300,698 500,680 C750,656 950,560 1200,518"
          fill="none" stroke="#1b1d52" stroke-width="14" opacity="0.55" filter="url(#wave-shadow)"/>
    <path d="M0,620 C150,680 300,702 500,684 C750,660 950,562 1200,522 L1200,750 L0,750 Z"
          fill="#ffffff"/>
    <path d="M0,620 C150,680 300,702 500,684 C750,660 950,562 1200,522"
          fill="none" stroke="#23215f" stroke-width="4"/>
  </svg>

  <div class="emblem" role="img" aria-label="Grosses, dezentes Praxis-Emblem als Hintergrundmotiv">
    <span class="emblem__name">Kieferorthopädie Tannwiese</span>
  </div>

  <div class="practice__marker" aria-hidden="true"></div>
  <h1 class="practice__name">Kieferorthopädie Tannwiese</h1>
  <p class="practice__doctor">Dr. med. dent. Lukas Brenner</p>
  <p class="practice__title">Fachzahnarzt für Kieferorthopädie (CH)</p>

  <div class="contact">
    <svg class="contact__icon" viewBox="0 0 32 28" aria-hidden="true">
      <path d="M2 9 C2 3 30 3 30 9 L30 12 L23 12 L23 8 C19 6.5 13 6.5 9 8 L9 12 L2 12 Z" fill="#3fabe2"/>
      <path d="M10 11 L22 11 L28 24 L4 24 Z" fill="#3fabe2"/>
      <g fill="#ffffff">
        <rect x="11" y="14" width="2.4" height="2.2"/>
        <rect x="14.8" y="14" width="2.4" height="2.2"/>
        <rect x="18.6" y="14" width="2.4" height="2.2"/>
        <rect x="10.2" y="17.6" width="2.4" height="2.2"/>
        <rect x="14.8" y="17.6" width="2.4" height="2.2"/>
        <rect x="19.4" y="17.6" width="2.4" height="2.2"/>
      </g>
    </svg>
    <span class="contact__phone">044 555 21 90</span>
  </div>
</main>
</body>
</html>
```